Inclusive life skills courses upskilling in wellbeing, academic success and career readines

I need a web design that is corporate and engaging. It needs to capture what we do and our core course offering. We develop courses and make customised course provision that cultivate 21st-century competencies that support academic achievement and social and emotional skills fostering personal growth and academic skill development that are relevant and timely for the learner. This prepares them for present and future challenges and opportunities, while contributing to students’ career portfolio with an accredited, relevant and adaptive provision. Our initial course is a Level 1 course. Here are the tentative course details. The courses will be accessed through the site, it should be crisp, clear and simple.

Level 1 Grounded Growth Journey is part of the GVDM designed to equip students with essential life skills. Accredited and focused on social-emotional learning, academic skills, and work preparation, this program offers a comprehensive approach to student development.

Course Structure
Certificates: Six short courses (micro learning) each can be taken individually or as a whole offering.
Credit Integration: Completing all six courses cumulates credits.
Course Duration: Each course involves 3 hours of content, 6 hours of practical application, and 3 hours of portfolio work and reflection.
*Note REFO Tariff is possible with BTK L3. An accredited CPD course may be simpler.
Short Courses within Level 1 GVDM
Self-Awareness: A sense of purpose. understand emotions, thoughts, and values and how they influence behavior across contexts. This includes capacities to recognize one’s strengths and limitations with a well- grounded sense of confidence and purpose.
Self-Management: A sense of self. Manage emotions, and behaviors in different situations to achieve goals and aspirations while managing time, stress and balance.
Building Resilience: Overcome challenges and adversity. Develop the confidence to face life’s challenges and reach your full potential, feeling more capable and in control of your life
Motivation & Mindset: Cultivating a positive approach and drive. This requires effective study skills, a growth mindset, gratitude and techniques to find work life balance.
Communication: Build rapport. Approach different types of conversation with confidence and clarity, listen and relate to others and manage requests.
Making an Impact: Develop assertiveness and confidence. Confidently share your ideas and opinions, improve your influencing skills and explore the trust equation.
Skills badges in progress: problem-solving, leadership, teamwork, listening, aiming high, staying positive.
Approach
Student-Centric: Courses blend digital learning with practical application.
Flexibility: Self-paced, adaptable to independent or classroom learning.
Digital Integration: Includes digital portfolio of practice (DPP) and skill bite certificates.
Practical Application: Emphasizes real-world skills and portfolio building.
Progress monitoring: Students are empowered in their learning and development.
Customization: AI-driven to tailor courses to student needs.
Aim and Impact
This qualification is designed to be directly relevant and applicable to students’ daily lives, encouraging personal growth and skill development. It’s a flexible offering, which is self-paced or blended (flipped) with the practical components integrated into classes. Teachers and students experience flipped learning and then practice and develop portfolio through subject teaching.

Progression Levels (BTK or CPD)

Level 1 Training for Life and Work (CPD Credits)
Level 2 Project Management and Teamwork (CPD Credits)
Level 3 Leading, Mentoring, Coaching
Level 4 Innovative Entrepreneurship

Please note: A logo will be available. The colour branding is similar to this:https://tavorlane.com/ and this: https://brimquell.com/

Education (K-12, university and corporate)

1 page

Serif

0054AA
0677BA
7BADD7
CADEEF
E8F1F8
0094D4
00A9DD
6FCCEA
C7EBF8
E9F6FB
00AB8E
00BBA5
67D7C9
C6EFE9
E9F9F6

• Simple, captures what we do.

```html
<!DOCTYPE html>
<html lang="en">
<head>
<meta charset="utf-8">
<title>Northbeam Skills – Life Skills Training</title>
<link href="https://fonts.googleapis.com/css2?family=Roboto+Slab:wght@400;500;600;700&display=swap" rel="stylesheet">
<style>
:root{
  --brand:#0054AA;
  --brand-mid:#0677BA;
  --sky:#7BADD7;
  --mist:#E8F1F8;
  --navy:#0a2352;
  --navy-deep:#041633;
  --ink:#111111;
  --text:#444444;
  --muted:#777777;
  --white:#ffffff;
  --footer:#000000;
}
*{margin:0;padding:0;box-sizing:border-box}
html,body{width:1200px;height:3963px;overflow:hidden}
body{font-family:"Roboto Slab",Georgia,serif;color:var(--ink);background:var(--white);position:relative}
.abs{position:absolute}
a{color:inherit;text-decoration:none}

/* header */
.top-rule{left:0;top:0;width:1200px;height:6px;background:#9a9a9a}
.util-tab{left:761px;top:0;width:320px;height:31px;background:#8c8c8c;clip-path:polygon(0 0,100% 0,94% 100%,6% 100%);color:var(--white);font-size:13px;display:flex;justify-content:center;align-items:center;gap:10px}
.logo{left:111px;top:18px;display:flex;align-items:center;gap:10px}
.logo-ring{width:66px;height:66px;border-radius:50%;border:4px solid var(--brand)}
.logo-name{font-size:20px;font-weight:500;color:var(--navy);letter-spacing:1px}
.nav{left:350px;top:52px;display:flex;gap:32px;font-size:16px;color:var(--ink)}
.nav .active{color:var(--brand)}
.search{left:866px;top:51px}
.btn-primary{left:917px;top:43px;width:170px;height:39px;border-radius:20px;background:var(--brand);color:var(--white);font-size:16px;display:flex;align-items:center;justify-content:center}

/* hero */
.hero{left:0;top:95px;width:1200px;height:599px;background:radial-gradient(circle at 78% 30%,#2a7fd6 0%,#0c3c85 30%,#062a66 60%,#041c4a 100%)}
.hero h1{position:absolute;left:111px;top:68px;font-size:54px;line-height:59px;font-weight:600;color:var(--white)}
.hero .btn-light{position:absolute;left:112px;top:277px;width:171px;height:39px;border-radius:20px;background:var(--white);color:var(--brand);font-size:16px;display:flex;align-items:center;justify-content:center}

/* offer */
.section-title{width:1200px;text-align:center;font-weight:600;font-size:40px;left:0}
.offer-bg{left:250px;top:840px;width:700px;height:347px;background:radial-gradient(ellipse,#eef4fa 0%,#ffffff 70%)}
.offer{top:851px;width:240px;text-align:center}
.offer .icon{width:98px;height:98px;margin:0 auto;border-radius:50%;border:4px solid #e4e9ef;border-left-color:#cfd8e2;display:flex;align-items:center;justify-content:center}
.offer .icon.on{border-color:var(--brand);border-right-color:#e4e9ef}
.offer h3{margin-top:20px;font-size:21px;font-weight:500;line-height:28px}
.offer p{margin-top:6px;font-size:15px;line-height:22px;color:var(--muted)}

/* purpose */
.purpose{left:0;top:1187px;width:1200px;height:625px;background:linear-gradient(180deg,#0a3466 0%,#082a58 50%,#04183a 100%)}
.purpose h2{position:absolute;top:50px;width:1200px;text-align:center;font-size:40px;font-weight:600;color:var(--white)}
.purpose p{position:absolute;left:126px;width:948px;text-align:center;font-size:15.5px;line-height:22px;color:var(--white)}
.purpose .map{position:absolute;left:100px;top:290px;width:1010px;height:335px;border-radius:500px 500px 0 0;background:radial-gradient(ellipse at 50% 60%,#0e5a8e 0%,#0a3a6a 45%,rgba(4,24,58,0) 75%)}

/* courses */
.tab{top:1961px;height:36px;border-radius:18px;font-size:15px;font-weight:500;display:flex;align-items:center;justify-content:center}
.tab.outline{left:338px;width:248px;border:2px solid var(--brand);color:var(--brand)}
.tab.fill{left:614px;width:247px;background:var(--brand);color:var(--white)}
.course{top:2032px;width:310px}
.course .photo{width:308px;height:209px}
.course h3{margin-top:30px;font-size:21px;line-height:28px;font-weight:600;color:var(--brand-mid)}
.course ul{margin-top:8px;list-style:none}
.course li{font-size:15px;line-height:30px;color:var(--ink);padding-left:35px;position:relative}
.course li::before{content:"";position:absolute;left:18px;top:13px;width:6px;height:6px;border-radius:50%;background:var(--brand-mid)}

/* provider */
.provider-title{left:111px;top:2553px;font-size:42px;line-height:46px;font-weight:600}
.provider-sub{left:111px;top:2651px;font-size:15px;color:var(--text)}
.feature{left:111px;width:590px;display:flex;gap:10px}
.feature .ficon{width:44px;flex:none}
.feature h4{font-size:19px;font-weight:600;line-height:26px}
.feature p{font-size:13px;line-height:19px;color:var(--text);margin-top:4px}
.provider-ring{left:672px;top:2549px;width:700px;height:501px;border-radius:260px 0 0 260px;background:var(--brand)}
.provider-photo{left:686px;top:2549px;width:600px;height:501px;border-radius:250px 0 0 250px;background:radial-gradient(circle at 50% 45%,#c96a5a 0%,#7a62a8 30%,#2c4ea6 60%,#1e3a8c 100%)}

/* founders */
.founder{top:3207px;width:476px;height:197px;border:2px solid #d4d4d4;border-radius:6px;padding:30px 32px}
.founder p{font-size:15px;line-height:26px;color:var(--muted)}
.founder .who{display:flex;align-items:center;gap:22px;margin-top:20px}
.founder .avatar{width:74px;height:74px;border-radius:50%;background:linear-gradient(160deg,#c9c3bd,#6f6a66)}
.founder .name{font-size:14px;font-weight:600;color:var(--brand)}
.founder .more{font-size:12px;color:var(--text);margin-top:10px}
.dots{left:582px;top:3433px;display:flex;gap:6px;align-items:center}
.dots span{height:5px;border-radius:3px;background:var(--brand)}

/* footer */
.footer{left:0;top:3527px;width:1200px;height:380px;background:var(--footer);color:var(--white)}
.footer .f-logo{position:absolute;left:112px;top:116px;display:flex;align-items:center;gap:12px}
.footer .f-logo .ring{width:96px;height:96px;border-radius:50%;border:4px solid var(--white)}
.footer .f-logo span{font-size:26px;font-weight:500;letter-spacing:1px}
.footer .about{position:absolute;left:112px;top:222px;width:310px;font-size:15px;line-height:26px}
.footer h5{position:absolute;top:84px;font-size:21px;font-weight:600}
.footer .links{position:absolute;left:478px;top:142px;font-size:15px;line-height:26px;list-style:none}
.footer .contact{position:absolute;left:698px;width:200px;font-size:13px;line-height:21px;padding-left:26px}
.footer .contact b{font-size:17px;font-weight:500;display:block;line-height:22px}
.footer .contact svg{position:absolute;left:0;top:4px}
.footer .social{position:absolute;left:983px;font-size:14px;display:flex;align-items:center;gap:18px}
.footer .social i{width:22px;height:22px;background:var(--white);border-radius:3px;display:block}
.copyright{left:0;top:3907px;width:1200px;height:56px;background:var(--brand-mid);color:var(--white);font-size:14px;display:flex;align-items:center;justify-content:center}
</style>
</head>
<body>

<!-- header -->
<div class="abs top-rule"></div>
<div class="abs util-tab"><span>Contact Us</span><span>|</span><span>Contact Support</span><span>|</span><span>Log In</span></div>
<div class="abs logo"><div class="logo-ring"></div><span class="logo-name">Northbeam Skills</span></div>
<nav class="abs nav"><a class="active">Home</a><a>About Us</a><a>Our Courses</a><a>What We Do</a><a>Contact Us</a></nav>
<svg class="abs search" width="20" height="20" viewBox="0 0 20 20" aria-label="Search"><circle cx="8" cy="8" r="6" fill="none" stroke="#0054AA" stroke-width="2"/><line x1="12.5" y1="12.5" x2="18" y2="18" stroke="#0054AA" stroke-width="2.2"/></svg>
<a class="abs btn-primary">Get Started</a>

<!-- hero -->
<section class="abs hero" role="img" aria-label="Glowing digital globe with network lines over a deep blue background">
  <h1>Grow Personally<br>Develop Academically<br>Succeed Professionally</h1>
  <a class="btn-light">Get Started</a>
</section>

<!-- offer -->
<div class="abs offer-bg" role="img" aria-label="Faint world map backdrop"></div>
<h2 class="abs section-title" style="top:773px">We Offer Life Skills Training In</h2>

<div class="abs offer" style="left:78px">
  <div class="icon"><svg width="56" height="44" viewBox="0 0 56 44"><circle cx="14" cy="12" r="6" fill="#0054AA"/><circle cx="30" cy="10" r="6" fill="#0054AA"/><path d="M4 36c0-9 6-14 10-14s10 5 10 14z" fill="#0054AA"/><path d="M20 34c0-9 6-14 10-14s10 5 10 14z" fill="#0054AA"/><path d="M34 30l8-10 6 4 6-10" stroke="#0094D4" stroke-width="3" fill="none"/></svg></div>
  <h3>Personal<br>Growth</h3>
  <p>Self awareness,work-life balance,teamwork &amp;coaching</p>
</div>
<div class="abs offer" style="left:349px">
  <div class="icon on"><svg width="46" height="52" viewBox="0 0 46 52"><path d="M23 4a15 15 0 0 0-9 27v7h18v-7a15 15 0 0 0-9-27z" fill="#0054AA"/><rect x="15" y="41" width="16" height="4" fill="#0054AA"/><rect x="18" y="47" width="10" height="3" fill="#0054AA"/></svg></div>
  <h3>Elevating Academic<br>Skills</h3>
  <p>Self management<br>Motivation Study skills<br>Leadership</p>
</div>
<div class="abs offer" style="left:620px">
  <div class="icon"><svg width="48" height="48" viewBox="0 0 48 48"><rect x="8" y="10" width="24" height="32" rx="2" fill="#0054AA"/><line x1="13" y1="20" x2="27" y2="20" stroke="#fff" stroke-width="2"/><line x1="13" y1="27" x2="27" y2="27" stroke="#fff" stroke-width="2"/><circle cx="36" cy="12" r="9" fill="#0094D4"/><path d="M32 12l3 3 5-6" stroke="#fff" stroke-width="2" fill="none"/></svg></div>
  <h3>Career<br>Readiness</h3>
  <p>Aligning goals<br>Decision-making<br>Leadership Portfolio<br>planning</p>
</div>
<div class="abs offer" style="left:888px">
  <div class="icon"><svg width="48" height="44" viewBox="0 0 48 44"><path d="M24 6L2 16l22 10 22-10z" fill="#0054AA"/><path d="M12 22v10c6 6 18 6 24 0V22l-12 6z" fill="#0054AA"/></svg></div>
  <h3>Customized<br>Courses</h3>
  <p>Life Skills courses designed and aligned to needs and local accreditation</p>
</div>

<!-- purpose -->
<section class="abs purpose">
  <h2>Our&nbsp; Purpose</h2>
  <p style="top:118px">To elevate life skills learning by enabling it’s integration.Rather than dictating specific life skills, we strive to understand the core values and emerging needs of schools and nations. We bridge the gap between these values and needs with relevant life skills courses, supporting students in becoming autonomous, self-directed learners who can take charge of their lives.</p>
  <p style="top:196px">Our vision is for students, schools and nations to engage with life skills learning, elevating it’s important by integrating it as a subject with extrinsic value. Enabling students to access essential life skills supporting their well-being, academic studies and career- readiness.</p>
  <div class="map" role="img" aria-label="Glowing network map of the globe"></div>
</section>

<!-- courses -->
<h2 class="abs section-title" style="top:1890px">Our Courses</h2>
<div class="abs tab outline">Sample Course Pathways</div>
<div class="abs tab fill">Sample Courses</div>

<article class="abs course" style="left:111px">
  <div class="photo" role="img" aria-label="Staircase rising toward a glowing arrow on a dark wall" style="background:linear-gradient(135deg,#5a6a82 0%,#3c4654 55%,#a88c4a 100%)"></div>
  <h3>Personal Growth: Skills for Life &amp;Study</h3>
  <ul><li>Self Awareness</li><li>Self Management</li><li>Motivation &amp; Resilience</li><li>Learning to Learn</li><li>Work- Life Balance</li></ul>
</article>
<article class="abs course" style="left:444px">
  <div class="photo" role="img" aria-label="Laptop resting on a stack of books against a blue background" style="background:linear-gradient(160deg,#5fd0ef 0%,#1ea9d8 50%,#2a6b8a 100%)"></div>
  <h3>Academics: Making an Impact</h3>
  <ul><li>Communication &amp; Confidence</li><li>Student leadership</li><li>Peer Coaching</li><li>Managing and Scaling Projects</li><li>Making an Impact</li></ul>
</article>
<article class="abs course" style="left:777px">
  <div class="photo" role="img" aria-label="Hand holding a glowing light bulb with network lines" style="background:radial-gradient(circle at 25% 30%,#f3d2b8 0%,#7fb3ad 35%,#2f8a8c 100%)"></div>
  <h3>Career Readiness: Identifying Pathways</h3>
  <ul><li>Goal Alignment &amp; Decision-making</li><li>Planning a supercurricula portfolio</li><li>Integrated Skill Training</li><li>Exploring&nbsp; Career Pathways</li><li>Entreprenuer ship &amp; Future visioning</li></ul>
</article>

<!-- provider -->
<h2 class="abs provider-title">Life Skills Training<br>Provider</h2>
<p class="abs provider-sub">Inclusive courses cultivating skills to live healthy, productive lives</p>

<div class="abs feature" style="top:2700px">
  <svg class="ficon" width="44" height="44" viewBox="0 0 44 44"><circle cx="22" cy="22" r="20" fill="#0054AA"/><circle cx="22" cy="22" r="7" fill="#fff"/></svg>
  <div><h4>Expert Leadership Team</h4><p>An expert team including Dr Daniel Orrin , Leila Brannock, Ruth Calder, Simon Ferrow, who bring a wealth of experience in education and innovation.</p></div>
</div>
<div class="abs feature" style="top:2795px">
  <svg class="ficon" width="44" height="44" viewBox="0 0 44 44"><circle cx="22" cy="10" r="6" fill="#0054AA"/><rect x="8" y="20" width="28" height="6" fill="#0054AA"/><rect x="14" y="28" width="16" height="14" fill="#0054AA"/></svg>
  <div><h4>Accredited Experiential Training</h4><p>Unlocking talent through an experiential and reflective<br>approach that is self-paced,evidenced, relevant and easy to use.</p></div>
</div>
<div class="abs feature" style="top:2880px">
  <svg class="ficon" width="44" height="44" viewBox="0 0 44 44"><path d="M22 6a12 12 0 0 0-7 22v6h14v-6a12 12 0 0 0-7-22z" fill="#0054AA"/><rect x="16" y="36" width="12" height="4" fill="#0054AA"/></svg>
  <div><h4>Purpose-driven</h4><p>Equipping learners with the skills needed to live healthy and successful<br>lives. Courses guide students to discover a rounder sense of purpose.</p></div>
</div>
<div class="abs feature" style="top:2966px">
  <svg class="ficon" width="44" height="44" viewBox="0 0 44 44"><rect x="4" y="10" width="36" height="26" fill="none" stroke="#0054AA" stroke-width="3"/><line x1="22" y1="10" x2="22" y2="36" stroke="#0054AA" stroke-width="3"/><rect x="9" y="15" width="8" height="16" fill="#0054AA"/></svg>
  <div><h4>Keeping Pace</h4><p>Customized Courses that align to core values and emerging societal competencies<br>of schools, education systems,governments and society,</p></div>
</div>

<div class="abs provider-ring"></div>
<div class="abs provider-photo" role="img" aria-label="Brain shape built from colourful cubes joined by network lines on blue"></div>

<!-- founders -->
<h2 class="abs section-title" style="top:3124px">Meet The Founders</h2>
<div class="abs founder" style="left:112px">
  <p>Dr. Daniel Orrin, earned his Doctorate in Space Technology from the Ardmoor University.</p>
  <div class="who"><div class="avatar" role="img" aria-label="Portrait photo of Daniel Orrin"></div><div><div class="name">Daniel Orrin</div><div class="more">Read More...</div></div></div>
</div>
<div class="abs founder" style="left:612px">
  <p>Founded Harlow Vale Sixth Form College (HVSC) in 2008. HVSC first topped the UK A-level league tables in 2010,....</p>
  <div class="who"><div class="avatar" role="img" aria-label="Portrait photo of Leila Brannock"></div><div><div class="name">Leila Brannock</div><div class="more">Read More...</div></div></div>
</div>
<div class="abs dots"><span style="width:24px"></span><span style="width:5px;background:#9bb6d6"></span></div>

<!-- footer -->
<footer class="abs footer">
  <div class="f-logo"><div class="ring"></div><span>Northbeam Skills</span></div>
  <p class="about">Global changes, evolving demographics, technological advancements, and shifting economic landscapes are shaping our present and future.</p>

  <h5 style="left:478px">Quick Links</h5>
  <ul class="links"><li>Home</li><li>About Us</li><li>Our Courses</li><li>What We Do</li><li>Contact Us</li></ul>

  <h5 style="left:698px">Contact Details</h5>
  <div class="contact" style="top:134px">
    <svg width="14" height="18" viewBox="0 0 14 18"><path d="M7 1a6 6 0 0 0-6 6c0 4 6 10 6 10s6-6 6-10a6 6 0 0 0-6-6z" fill="#fff"/><circle cx="7" cy="7" r="2" fill="#000"/></svg>
    <b>Address</b>123, Meridane GVDM<br>adipiscing elit.506301
  </div>
  <div class="contact" style="top:210px">
    <svg width="14" height="14" viewBox="0 0 14 14"><path d="M3 1l3 3-2 2c1 2 2 3 4 4l2-2 3 3-2 2C6 13 1 8 1 3z" fill="#fff"/></svg>
    <b>Phone</b>+1 555 014 2270
  </div>
  <div class="contact" style="top:264px">
    <svg width="15" height="11" viewBox="0 0 15 11"><rect width="15" height="11" fill="#fff"/><path d="M0 0l7.5 6L15 0" stroke="#000" fill="none"/></svg>
    <b>Email</b>info@meridanegvdm.com
  </div>

  <h5 style="left:983px">Follow Us</h5>
  <div class="social" style="top:138px"><i></i>Chirpline</div>
  <div class="social" style="top:184px"><i></i>Workgrid</div>
  <div class="social" style="top:230px"><i></i>Pagebook</div>
</footer>
<div class="abs copyright">Copyright © 2024 Meridane GVDM. All rights reserved.</div>

</body>
</html>
```